Plumwave business card

We need a modern business card - With our 4 colors - See web: www.plumwave.dk

I have attached logo and som old business Cards we have - Lets Make the new ones shine...:-) -

Industry/Entity Type

Business

Requirements
Must have
• the logo with plumwave only,

```html
<!DOCTYPE html>
<html lang="da">
<head>
<meta charset="utf-8">
<title>Plumwave business card</title>
<link rel="stylesheet" href="https://fonts.googleapis.com/css2?family=Open+Sans:wght@300;400;600&display=swap">
<style>
  :root {
    --lime: #8cc63f;
    --lime-light: #a4d65e;
    --plum: #c2288a;
    --white: #ffffff;
    --ink: #3a3a3a;
    --stage: #eeeeea;
  }
  * { box-sizing: border-box; margin: 0; padding: 0; }
  html, body {
    width: 1200px; height: 900px; overflow: hidden;
    background: var(--stage);
    font-family: "Open Sans", sans-serif;
  }
  .canvas { position: relative; width: 1200px; height: 900px; }

  .card {
    position: absolute;
    width: 640px; height: 366px;
    overflow: hidden;
    box-shadow: 0 10px 26px rgba(0,0,0,.18);
  }

  /* Back side */
  .card-back { left: 90px; top: 60px; background: var(--lime); }
  .card-back .brand {
    position: absolute; left: 330px; top: 118px;
    color: var(--white); font-weight: 300;
    font-size: 24px; letter-spacing: 4px;
  }
  .card-back .rule {
    position: absolute; left: 320px; top: 160px;
    width: 270px; height: 3px; background: var(--white);
  }
  .card-back .tagline {
    position: absolute; left: 430px; top: 172px;
    color: var(--white); font-size: 15px; letter-spacing: .5px;
  }

  /* Front side */
  .card-front { left: 470px; top: 470px; background: var(--lime); }
  .card-front .shape { position: absolute; inset: 0; }
  .logo {
    position: absolute; left: 290px; top: 62px; width: 250px;
    text-align: center;
  }
  .logo .brand {
    display: inline-flex; align-items: center; gap: 10px;
    color: var(--ink); font-size: 21px; letter-spacing: 4px;
  }
  .logo .dot {
    width: 12px; height: 12px; border-radius: 50%; background: var(--lime);
  }
  .logo .rule { height: 2px; background: var(--lime); margin: 8px 0 10px; }
  .logo .tagline { color: var(--ink); font-size: 12px; letter-spacing: .5px; }

  .person { position: absolute; left: 92px; top: 100px; }
  .person .name { color: var(--lime); font-weight: 600; font-size: 24px; line-height: 1.1; }
  .person .role { color: var(--ink); font-size: 18px; }

  .contacts {
    position: absolute; left: 70px; top: 212px; list-style: none;
    color: var(--ink); font-size: 18px;
  }
  .contacts li { display: flex; align-items: center; gap: 12px; height: 30px; }
  .contacts svg { width: 16px; height: 16px; flex: none; }
</style>
</head>
<body>
<main class="canvas">

  <section class="card card-back" aria-label="Card back">
    <p class="brand">plumwave</p>
    <div class="rule"></div>
    <p class="tagline">medier til unge</p>
  </section>

  <section class="card card-front" aria-label="Card front">
    <svg class="shape" viewBox="0 0 640 366" aria-hidden="true">
      <path d="M0,366 L0,175 C60,70 200,12 400,10 L540,10 C610,14 640,70 640,130 C640,230 560,330 400,366 Z" fill="var(--white)"/>
      <path d="M0,188 C70,80 190,18 340,0" fill="none" stroke="var(--plum)" stroke-width="8"/>
      <path d="M0,206 C80,96 200,30 360,8" fill="none" stroke="var(--white)" stroke-width="3"/>
      <path d="M390,366 C530,330 615,255 640,160" fill="none" stroke="var(--plum)" stroke-width="8"/>
    </svg>

    <div class="logo">
      <span class="brand"><span class="dot"></span>plumwave</span>
      <div class="rule"></div>
      <p class="tagline">medier til unge</p>
    </div>

    <div class="person">
      <p class="name">Add Name</p>
      <p class="role">Manager</p>
    </div>

    <ul class="contacts">
      <li>
        <svg viewBox="0 0 16 16" aria-hidden="true"><path d="M4 1 L6.5 4 L5 6 C6 8.5 7.5 10 10 11 L12 9.5 L15 12 L13 15 C7 14.5 1.5 9 1 3 Z" fill="var(--lime)"/></svg>
        <span>40 12 34 56</span>
      </li>
      <li>
        <svg viewBox="0 0 16 16" aria-hidden="true"><g fill="none" stroke="var(--lime)" stroke-width="1.4"><circle cx="8" cy="8" r="6.5"/><ellipse cx="8" cy="8" rx="3" ry="6.5"/><path d="M1.5 8 H14.5"/></g></svg>
        <span>www.plumwave.dk</span>
      </li>
      <li>
        <svg viewBox="0 0 16 16" aria-hidden="true"><text x="8" y="13" text-anchor="middle" font-size="15" font-family="Open Sans, sans-serif" font-weight="600" fill="var(--lime)">@</text></svg>
        <span>er@plumwave.com</span>
      </li>
    </ul>
  </section>

</main>
</body>
</html>
```